Webdesign für Juwelier-Geschäft
Zielgruppe
Wir sind ein Juwelier Laden. Unsere Zielgruppe sind Frauen und Männer jeden Alters, die an Gold- und Silberschmuck/Uhren/Diamanten/Trauringen interessiert sind.
Aufgabenstellung
Edles Design in Gold, Schwarz/Grau, Weiß.
Bildelemente für die Artikelkategorien Ketten, Ohrringe und Ringe etc.
Ein Logo besteht bereits.

```html
<!DOCTYPE html>
<html lang="de">
<head>
<meta charset="utf-8">
<title>Juwelier Orion</title>
<link href="https://fonts.googleapis.com/css2?family=Cinzel:wght@400;500&family=Lato:wght@400;700;900&display=swap" rel="stylesheet">
<style>
:root{
  --gold:#e9c46a;
  --gold-deep:#c9a14a;
  --gold-text:#a88a4a;
  --ink:#1b1b1b;
  --dark:#141414;
  --line:#d9d9d9;
  --white:#fff;
}
*{box-sizing:border-box;margin:0;padding:0}
html,body{width:1200px;height:2682px;overflow:hidden;background:var(--white);font-family:'Lato',sans-serif;color:var(--ink)}
.page{position:relative;width:1200px;height:2682px}

/* hero */
.hero{position:absolute;left:0;top:0;width:1200px;height:508px;background:linear-gradient(90deg,#151515 0%,#1c1c1c 50%,#262626 100%);overflow:hidden}
.hero-visual{position:absolute;left:640px;top:0;width:560px;height:508px;
  background:
    radial-gradient(ellipse 130px 70px at 62% 78%,rgba(200,130,60,.75) 0%,rgba(200,130,60,0) 100%),
    radial-gradient(ellipse 210px 260px at 52% 35%,#bdbdbd 0%,#8c8c8c 40%,#4a4a4a 70%,rgba(40,40,40,0) 100%),
    linear-gradient(90deg,rgba(30,30,30,1) 0%,rgba(30,30,30,0) 25%,rgba(230,230,230,.35) 100%)}
.brand{position:absolute;left:151px;top:20px;font-family:'Cinzel',serif;color:var(--gold)}
.brand-name{font-size:21px;line-height:22px;letter-spacing:1px}
.brand-sub{font-family:'Lato',sans-serif;font-size:8px;letter-spacing:.3px;margin-top:6px}
.cart{position:absolute;left:974px;top:24px;color:#fff;font-size:10px;display:flex;align-items:center;gap:3px}
.menu-btn{position:absolute;left:1016px;top:20px;width:34px;height:26px;border:1px solid #777;display:flex;flex-direction:column;align-items:flex-end;justify-content:center;gap:3px;padding-right:8px}
.menu-btn span{display:block;height:2px;background:var(--gold)}
.hero-title{position:absolute;left:150px;top:217px;border-left:3px solid var(--gold);padding-left:18px;font-family:'Cinzel',serif;font-weight:400;font-size:42px;line-height:45px;letter-spacing:1px}
.hero-title .w{color:#fff}
.hero-title .g{color:var(--gold)}
.dots{position:absolute;left:561px;top:469px;display:flex;gap:9px}
.dots span{width:8px;height:8px;border-radius:50%;border:1px solid #bbb}
.dots span.on{background:var(--gold);border-color:var(--gold)}

/* categories */
.cats{position:absolute;left:150px;top:536px;width:901px;height:118px;border:1px solid var(--line);display:flex}
.cat{border-right:1px solid var(--line);position:relative;text-align:center}
.cat:last-child{border-right:none}
.cat-art{position:absolute;left:50%;top:8px;transform:translateX(-50%);width:64px;height:64px;border-radius:50%;background:radial-gradient(circle,#f6dc8f 0%,#e2b44e 45%,rgba(226,180,78,0) 72%)}
.cat-label{position:absolute;left:0;right:0;top:90px;font-size:12px;font-weight:700;letter-spacing:.3px}

/* about */
.about-mark{position:absolute;left:177px;top:703px;width:140px;height:249px;display:flex;align-items:center;justify-content:center;font-weight:700;color:var(--gold);font-size:15px;letter-spacing:1px;text-align:center}
.about-title{position:absolute;left:376px;top:742px;font-size:27px;font-weight:700;color:var(--gold);letter-spacing:.3px}
.about-text{position:absolute;left:376px;top:786px;width:670px;font-size:11.5px;line-height:22.5px;color:#333}

/* shop */
.section-title{position:absolute;left:0;width:1200px;text-align:center;font-size:27px;font-weight:700;color:var(--gold);letter-spacing:.3px}
.grid{position:absolute;left:150px;top:1068px;display:grid;grid-template-columns:repeat(4,206px);grid-auto-rows:201px;column-gap:25px;row-gap:26px}
.card{border:1px solid #e3e3e3;position:relative;text-align:center}
.card-art{position:absolute;left:50%;top:20px;transform:translateX(-50%);width:118px;height:96px;border-radius:45%;background:radial-gradient(ellipse,#f0d38a 0%,#b98a3c 50%,rgba(185,138,60,0) 72%)}
.card-art.blue{background:radial-gradient(ellipse,#3da0e8 0%,#1c5fa8 30%,#c99a48 52%,rgba(201,154,72,0) 72%)}
.card-art.white{background:radial-gradient(ellipse,#ffffff 0%,#dcdce6 25%,#e6c888 48%,rgba(230,200,136,0) 72%)}
.card-name{position:absolute;left:0;right:0;top:134px;font-size:12px;font-weight:700;color:var(--gold-text)}
.card-price{position:absolute;left:0;right:0;top:151px;font-size:22px;color:#222}

/* repair */
.repair{position:absolute;left:0;top:1753px;width:1200px;height:274px;background:linear-gradient(90deg,#3c4352 0%,#5b6270 40%,#4b515e 70%,#2f3440 100%);text-align:center;color:#fff}
.repair h2{position:absolute;left:0;right:0;top:88px;font-size:38px;font-weight:700}
.repair p{position:absolute;left:0;right:0;top:140px;font-size:14px}
.btn{position:absolute;background:var(--gold);color:var(--ink);border-radius:20px;display:flex;align-items:center;justify-content:center;gap:10px}
.repair .btn{left:486px;top:169px;width:228px;height:37px;font-size:18px}

/* promos */
.promo{position:absolute;top:2065px;width:428px;height:280px;overflow:hidden}
.promo.left{left:151px;background:radial-gradient(ellipse at 60% 45%,#d4ab52 0%,#8a6628 30%,#2a1614 68%)}
.promo.right{left:621px;background:radial-gradient(ellipse at 50% 60%,#c29240 0%,#6b3a2a 32%,#2a2522 70%)}
.badge-sale{position:absolute;left:0;top:92px;width:140px;height:96px;background:var(--gold);border-radius:0 48px 48px 0;padding:8px 0 0 22px;color:var(--ink);line-height:1}
.badge-sale .s{font-size:18px}
.badge-sale .b{font-size:44px;font-weight:900;margin:2px 0}
.badge-new{position:absolute;left:0;top:48px;height:50px;width:219px;background:var(--gold);border-radius:0 25px 25px 0;padding-left:21px;display:flex;align-items:center;font-size:19px;font-weight:700}
.promo .btn{left:220px;top:231px;width:192px;height:37px;font-size:15px;font-weight:700}

/* footer */
.footer{position:absolute;left:0;top:2395px;width:1200px;height:287px;background:#111;color:var(--gold)}
.f-mark{position:absolute;left:160px;top:80px;width:56px;height:56px;border:2px solid var(--gold)}
.f-name{position:absolute;left:258px;top:68px;font-family:'Cinzel',serif;font-size:24px;letter-spacing:1px}
.f-row{position:absolute;left:256px;display:flex;gap:10px;font-size:11px;line-height:15px;letter-spacing:.5px}
.f-row svg{flex:none;margin-top:2px}
.f-phone{font-size:19px;line-height:22px}
.news-title{position:absolute;left:548px;top:68px;font-size:12px;font-weight:700}
.news-field{position:absolute;left:548px;top:97px;width:268px;height:39px;background:#2a2a2a;border-radius:2px;display:flex;align-items:center;padding:0 12px;gap:9px;font-size:11px;color:#777}
.news-field .send{margin-left:auto}
.social{position:absolute;left:892px;top:64px;display:flex;gap:22px}
.social span{width:14px;height:14px;border-radius:50%;border:2px solid var(--gold)}
.f-rule{position:absolute;left:150px;top:236px;width:900px;height:1px;background:#2c2c2c}
.f-copy{position:absolute;left:150px;top:255px;font-size:11px;color:#bbb}
.f-legal{position:absolute;right:151px;top:255px;font-size:11px;color:#bbb}
</style>
</head>
<body>
<div class="page">

  <header class="hero">
    <div class="hero-visual" role="img" aria-label="Schwarz-Weiß-Porträtfoto einer Frau mit goldenem Collier, Ohrringen und Ring"></div>
    <div class="brand">
      <div class="brand-name">JUWELIER<br>ORION</div>
      <div class="brand-sub">TRAURINGE | UHREN | SCHMUCK</div>
    </div>
    <div class="cart">
      <svg width="16" height="13" viewBox="0 0 16 13"><path d="M1 1h2.5l2 7.5h8l1.5-5.5H4.5" fill="none" stroke="#fff" stroke-width="1.4"/><circle cx="6.5" cy="11.3" r="1.2" fill="#fff"/><circle cx="12.5" cy="11.3" r="1.2" fill="#fff"/></svg>(0)
    </div>
    <div class="menu-btn"><span style="width:9px"></span><span style="width:16px"></span><span style="width:12px"></span></div>
    <h1 class="hero-title">
      <span class="w">DUIS AUTE</span><br>
      <span class="g">IRURE DOLOR IN</span><br>
      <span class="g">REPREHENDERIT</span>
    </h1>
    <div class="dots"><span class="on"></span><span></span><span></span><span></span><span></span></div>
  </header>

  <nav class="cats">
    <div class="cat" style="width:129px"><div class="cat-art" role="img" aria-label="Goldene Kette"></div><div class="cat-label">KETTEN</div></div>
    <div class="cat" style="width:152px"><div class="cat-art" role="img" aria-label="Goldring mit Diamant"></div><div class="cat-label">RINGE</div></div>
    <div class="cat" style="width:167px"><div class="cat-art" role="img" aria-label="Zwei goldene Trauringe"></div><div class="cat-label">TRAURINGE</div></div>
    <div class="cat" style="width:158px"><div class="cat-art" role="img" aria-label="Goldene Taschenuhr"></div><div class="cat-label">UHREN</div></div>
    <div class="cat" style="width:160px"><div class="cat-art" role="img" aria-label="Goldene Ohrringe mit Perle"></div><div class="cat-label">OHRRINGE</div></div>
    <div class="cat" style="flex:1"><div class="cat-art" role="img" aria-label="Goldene Armbänder"></div><div class="cat-label">ARMBÄNDER</div></div>
  </nav>

  <section>
    <div class="about-mark">JUWELIER<br>ORION</div>
    <h2 class="about-title">WER WIR SIND</h2>
    <p class="about-text">Lorem ipsum dolor sit amet, consectetur adipiscing elit, sed do eiusmod tempor incididunt ut labore et dolore magna aliqua. Ut enim ad minim veniam, quis nostrud exercitation ullamco laboris nisi ut aliquip ex ea commodo consequat. Duis aute irure dolor in repre&shy;henderit in voluptate velit esse cillum dolore eu fugiat nulla pariatur. Excepteur sint occaecat cupidatat non proident, sunt in culpa qui officia deserunt mollit anim id est laborum.</p>
  </section>

  <section>
    <h2 class="section-title" style="top:1000px">JETZT EINKAUFEN</h2>
    <div class="grid">
      <div class="card"><div class="card-art blue" role="img" aria-label="Goldring mit blauem Stein"></div><div class="card-name">Ring Herren, 585 Gold</div><div class="card-price">€ 499.00</div></div>
      <div class="card"><div class="card-art" role="img" aria-label="Goldener Herrenring mit Steinbesatz"></div><div class="card-name">Ring Herren, 585 Gold</div><div class="card-price">€ 499.00</div></div>
      <div class="card"><div class="card-art" role="img" aria-label="Goldener Siegelring"></div><div class="card-name">Ring Herren, 585 Gold</div><div class="card-price">€ 499.00</div></div>
      <div class="card"><div class="card-art white" role="img" aria-label="Goldring mit weißem Stein"></div><div class="card-name">Ring Herren, 585 Gold</div><div class="card-price">€ 499.00</div></div>
      <div class="card"><div class="card-art white" role="img" aria-label="Goldring mit weißem Stein"></div><div class="card-name">Ring Herren, 585 Gold</div><div class="card-price">€ 499.00</div></div>
      <div class="card"><div class="card-art" role="img" aria-label="Goldener Siegelring"></div><div class="card-name">Ring Herren, 585 Gold</div><div class="card-price">€ 499.00</div></div>
      <div class="card"><div class="card-art" role="img" aria-label="Goldener Herrenring mit Steinbesatz"></div><div class="card-name">Ring Herren, 585 Gold</div><div class="card-price">€ 499.00</div></div>
      <div class="card"><div class="card-art blue" role="img" aria-label="Goldring mit blauem Stein"></div><div class="card-name">Ring Herren, 585 Gold</div><div class="card-price">€ 499.00</div></div>
      <div class="card"><div class="card-art blue" role="img" aria-label="Goldring mit blauem Stein"></div><div class="card-name">Ring Herren, 585 Gold</div><div class="card-price">€ 499.00</div></div>
      <div class="card"><div class="card-art" role="img" aria-label="Goldener Herrenring mit Steinbesatz"></div><div class="card-name">Ring Herren, 585 Gold</div><div class="card-price">€ 499.00</div></div>
      <div class="card"><div class="card-art" role="img" aria-label="Goldener Siegelring"></div><div class="card-name">Ring Herren, 585 Gold</div><div class="card-price">€ 499.00</div></div>
      <div class="card"><div class="card-art white" role="img" aria-label="Goldring mit weißem Stein"></div><div class="card-name">Ring Herren, 585 Gold</div><div class="card-price">€ 499.00</div></div>
    </div>
  </section>

  <section class="repair" role="img" aria-label="Foto einer Goldschmiede-Werkbank mit Händen, die einen Ring bearbeiten">
    <h2>Reparaturen und Altgold-Ankauf</h2>
    <p>Duis aute irure dolor in reprehenderit in voluptate velit esse cillum dolore eu fugiat nulla pariatur.</p>
    <div class="btn">
      <svg width="16" height="16" viewBox="0 0 16 16"><path d="M4 2l2.5 3-1.5 1.5c.8 1.8 2.2 3.2 4 4l1.5-1.5 3 2.5-1.5 2C7 13 3 9 2 3.5z" fill="none" stroke="#333" stroke-width="1.2"/></svg>
      1800.987.654
    </div>
  </section>

  <section>
    <div class="promo left" role="img" aria-label="Foto eines goldenen Colliers mit grünen Steinen und passenden Ohrringen">
      <div class="badge-sale"><div class="s">Heute</div><div class="b">30 %</div><div class="s">Rabatt</div></div>
      <div class="btn">
        <svg width="18" height="15" viewBox="0 0 16 13"><path d="M1 1h2.5l2 7.5h8l1.5-5.5H4.5" fill="none" stroke="#222" stroke-width="1.4"/><circle cx="6.5" cy="11.3" r="1.2" fill="#222"/><circle cx="12.5" cy="11.3" r="1.2" fill="#222"/></svg>
        Jetzt einkaufen
      </div>
    </div>
    <div class="promo right" role="img" aria-label="Foto eines goldenen Anhängers mit roter Perlenkette auf dunklem Holz">
      <div class="badge-new">Neueste Kollektionen</div>
      <div class="btn">
        <svg width="18" height="15" viewBox="0 0 16 13"><path d="M1 1h2.5l2 7.5h8l1.5-5.5H4.5" fill="none" stroke="#222" stroke-width="1.4"/><circle cx="6.5" cy="11.3" r="1.2" fill="#222"/><circle cx="12.5" cy="11.3" r="1.2" fill="#222"/></svg>
        Jetzt einkaufen
      </div>
    </div>
  </section>

  <footer class="footer">
    <div class="f-mark"></div>
    <div class="f-name">JUWELIER ORION</div>
    <div class="f-row" style="top:98px">
      <svg width="13" height="16" viewBox="0 0 13 16"><path d="M6.5 1a5 5 0 0 1 5 5c0 3.5-5 9-5 9s-5-5.5-5-9a5 5 0 0 1 5-5z" fill="var(--gold)"/><circle cx="6.5" cy="6" r="2" fill="#111"/></svg>
      <div>xxxxxxxxxxxxxxxxxx<br>xxxxxxxxxxxxxxxxxxxxx<br>xxxxxxxxxxxxxxxxx</div>
    </div>
    <div class="f-row f-phone" style="top:150px">
      <svg width="15" height="15" viewBox="0 0 16 16"><path d="M4 2l2.5 3-1.5 1.5c.8 1.8 2.2 3.2 4 4l1.5-1.5 3 2.5-1.5 2C7 13 3 9 2 3.5z" fill="none" stroke="var(--gold)" stroke-width="1.3"/></svg>
      1800.987.654
    </div>
    <div class="f-row" style="top:185px">
      <svg width="13" height="13" viewBox="0 0 13 13"><path d="M12 1L1 6l4 1.5L6.5 12 12 1z" fill="none" stroke="var(--gold)" stroke-width="1.2"/></svg>
      xxxxxxxxxxxxxxxx
    </div>
    <div class="news-title">Melden Sie sich für unseren Newsletter an</div>
    <div class="news-field">
      <svg width="13" height="10" viewBox="0 0 13 10"><rect x=".5" y=".5" width="12" height="9" fill="none" stroke="#777"/><path d="M.5.5l6 5 6-5" fill="none" stroke="#777"/></svg>
      Geben sie ihre E-Mailadresse ein
      <svg class="send" width="14" height="14" viewBox="0 0 13 13"><path d="M12 1L1 6l4 1.5L6.5 12 12 1z" fill="none" stroke="var(--gold)" stroke-width="1.2"/></svg>
    </div>
    <div class="social"><span></span><span></span><span></span><span></span><span></span></div>
    <div class="f-rule"></div>
    <div class="f-copy">Copyright 2022. Alle Rechte vorbehalten.</div>
    <div class="f-legal">Impressum</div>
  </footer>

</div>
</body>
</html>
```